Meadowrun Honey labels

I have honey farm . I would like to sale it at grocery stores. I need really unique and very attractive designed labels, I would like to see writings 100% Natural honey and GMO free ,. Company name "MeadowrunHoney" . I want to put 2 labels and one ribbon tag in middle and round label on top of lid(only one diamond shape in the middle).I would like to see bee flying over red flower and at the left side flower field and right side bee putting honey into honey hives. I have attached example pictures of Honey Jars labels, tags and type. I have two different type of Honey jars i have also attached picture of those jars. For jar with red lid. If middle label little bit bigger than measurement thats ok because writing has to fit.

Target Market(s)

Grocery stores

Industry/Entity Type

Farm

Requirements
Must have
• 100% Natural Honey, GMO Free, Company name Meadowrun Honey, attractive and unique design. bee flying over flower, right side label flower field left side bee putting honey into bee hives.

```html
<!DOCTYPE html>
<html lang="en">
<head>
<meta charset="UTF-8">
<title>Meadowrun Honey – Lid Label</title>
<link rel="stylesheet" href="https://fonts.googleapis.com/css2?family=Cinzel:wght@400;600&family=Tinos&display=swap">
<style>
  :root {
    --backdrop: #f1f1f1;
    --label-red: #8d1a1f;
    --label-red-light: #a8282d;
    --label-red-dark: #6e1216;
    --ivory: #f6ede6;
    --honey-gold: #f2b52a;
  }
  * { margin: 0; padding: 0; box-sizing: border-box; }
  html, body { width: 1200px; height: 1200px; overflow: hidden; }
  body { background: var(--backdrop); position: relative; }

  .backdrop {
    position: absolute; inset: 0;
    background: var(--backdrop);
  }

  .lid-label {
    position: absolute;
    left: 6px; top: 6px;
    width: 1188px; height: 1188px;
    border-radius: 50%;
    background: radial-gradient(circle at 50% 42%, var(--label-red-light) 0%, var(--label-red) 55%, var(--label-red-dark) 100%);
  }

  .dotted-ring {
    position: absolute; left: 0; top: 0;
    width: 1200px; height: 1200px;
  }

  .brand-name {
    position: absolute;
    left: 0; width: 1200px;
    top: 250px;
    text-align: center;
    font-family: "Cinzel", serif;
    font-weight: 600;
    color: var(--honey-gold);
    line-height: 1;
  }
  .brand-name .brand-line-1 { display: block; font-size: 96px; letter-spacing: 2px; }
  .brand-name .brand-line-2 { display: block; font-size: 150px; margin-top: 20px; letter-spacing: 4px; }

  .claims {
    position: absolute;
    left: 0; width: 1200px;
    text-align: center;
    font-family: "Cinzel", serif;
    color: var(--ivory);
    line-height: 1;
  }
  .claim-percent { top: 698px; font-size: 72px; }
  .claim-natural { top: 768px; font-size: 62px; letter-spacing: 1px; }
  .claim-gmo { top: 858px; font-size: 78px; letter-spacing: 1px; }

  .net-weight {
    position: absolute;
    left: 0; width: 1200px;
    top: 962px;
    text-align: center;
    font-family: "Tinos", serif;
    color: var(--ivory);
    line-height: 1;
  }
  .net-weight .net-label { font-size: 38px; }
  .net-weight .net-value { font-size: 54px; }

  .dot-rule {
    position: absolute;
    left: 480px; top: 1040px;
    width: 240px; height: 30px;
  }
</style>
</head>
<body>
  <div class="backdrop" role="img" aria-label="Light honeycomb pattern background"></div>

  <div class="lid-label"></div>

  <svg class="dotted-ring" viewBox="0 0 1200 1200" aria-hidden="true">
    <circle cx="600" cy="600" r="556" fill="none" stroke="var(--ivory)" stroke-width="6"
            stroke-linecap="round" stroke-dasharray="0 14"/>
  </svg>

  <h1 class="brand-name">
    <span class="brand-line-1">Meadowrun</span>
    <span class="brand-line-2">Honey</span>
  </h1>

  <p class="claims claim-percent">100%</p>
  <p class="claims claim-natural">NATURAL HONEY</p>
  <p class="claims claim-gmo">GMO FREE</p>

  <p class="net-weight"><span class="net-label">Net weight : </span><span class="net-value">250g</span></p>

  <svg class="dot-rule" viewBox="0 0 240 30" aria-hidden="true">
    <line x1="20" y1="15" x2="220" y2="15" stroke="var(--honey-gold)" stroke-width="2" stroke-dasharray="0 10" stroke-linecap="round"/>
    <circle cx="8" cy="15" r="5" fill="var(--honey-gold)"/>
    <circle cx="120" cy="15" r="7" fill="var(--honey-gold)"/>
    <circle cx="232" cy="15" r="5" fill="var(--honey-gold)"/>
  </svg>
</body>
</html>
```